Design a styled business card for an intimacy and attachment psychologist

I am a Psychologist providing online therapy to patients across the United States. My work is interpersonal and emotion-focused, with an emphasis on the client-therapist relationship. My primary areas of work are very personal, including sexuality and gender, abuse and trauma, and grief and loss. My target audience will be adults of all ages 18+.
My business card should convey a warm and inviting feeling of professionalism that is also casual and comfortable.
The front should be fairly simple and professional, consisting of:
- My name, Dr. Rosalind Petrakis
- My title, Licensed Psycholigist
- My logo
On either the front or the back, my contact information should be listed:
- ros@drrospetrakis.example
- 555.014.7788
- drrospetrakis.example
On the rear, I would like a description of the areas that I specialize in. This can be formatted in any way that appears stylistically interesting.
Individual and Couples
Relationships and Infidelity
Sexual Health & Aging
Gender Identity & Sexual Orientation
Abuse and Trauma
Sexual Compulsivity & Addiction
Sexual Dysfunction
Target Market(s)
My target audience will be adults of all ages 18+.
Industry/Entity Type
Psychology
Contact Information for Business Card
The front should be fairly simple and professional, consisting of: - My name, Dr. Rosalind Petrakis - My title, Licensed Psycholigist - My logo On either the front or the back, my contact information should be listed: - ros@drrospetrakis.example - 555.014.7788 - drrospetrakis.example On the rear, I would like a description of the areas that I specialize in. This can be formatted in any way that appears stylistically interesting. Individual and Couples Relationships and Infidelity Sexual Health & Aging Gender Identity & Sexual Orientation Abuse and Trauma Sexual Compulsivity & Addiction Sexual Dysfunction
- Follow brand guide

```html
<!DOCTYPE html>
<html lang="en">
<head>
<meta charset="utf-8">
<title>Dr. Rosalind Petrakis – Business Cards</title>
<link rel="stylesheet" href="https://fonts.googleapis.com/css2?family=Cinzel:wght@500&family=Poppins:wght@300;400&display=swap">
<style>
  :root {
    --bg: #c4c4c6;
    --navy: #2b2450;
    --teal: #4dd5b5;
    --teal-light: #cdf1e8;
    --white: #ffffff;
    --shadow: rgba(0, 0, 0, 0.22);
  }
  * { margin: 0; padding: 0; box-sizing: border-box; }
  html, body { width: 1200px; height: 800px; overflow: hidden; }
  body {
    background: var(--bg);
    position: relative;
    font-family: "Poppins", sans-serif;
  }
  .card {
    position: absolute;
    left: 290px;
    width: 620px;
    height: 354px;
    border-radius: 22px;
    overflow: hidden;
    box-shadow: 0 10px 28px var(--shadow);
  }
  .card-front { top: 28px; background: var(--white); }
  .card-back { top: 418px; background: var(--navy); }

  .front-art { position: absolute; inset: 0; }

  .identity {
    position: absolute;
    left: 44px;
    top: 84px;
    color: var(--navy);
  }
  .identity-name {
    font-family: "Cinzel", serif;
    font-weight: 500;
    font-size: 25px;
    letter-spacing: 0.5px;
    line-height: 1.1;
  }
  .identity-title {
    font-weight: 300;
    font-size: 18px;
    margin-top: 2px;
  }

  .contact-list {
    position: absolute;
    left: 44px;
    top: 214px;
    list-style: none;
    color: var(--white);
    font-size: 15px;
    font-weight: 400;
    line-height: 24px;
  }
  .contact-list li { display: flex; align-items: center; gap: 10px; }
  .contact-icon { width: 15px; height: 15px; flex: none; }

  .logo-mark {
    position: absolute;
    left: 372px;
    top: 40px;
    width: 196px;
    height: 196px;
    display: flex;
    align-items: center;
    justify-content: center;
    text-align: center;
    font-family: "Cinzel", serif;
    font-weight: 500;
    font-size: 17px;
    line-height: 1.25;
    color: var(--navy);
    padding: 30px;
  }

  .back-brand {
    position: absolute;
    right: 40px;
    top: 42px;
    display: flex;
    align-items: center;
    gap: 16px;
  }
  .back-brand-dot {
    width: 64px;
    height: 64px;
    border-radius: 50%;
    background: var(--teal);
    border: 3px solid var(--white);
  }
  .back-brand-name {
    font-family: "Cinzel", serif;
    font-weight: 500;
    font-size: 30px;
    line-height: 1.05;
    color: var(--white);
  }

  .specialties {
    position: absolute;
    left: 40px;
    top: 150px;
    list-style: none;
    color: var(--white);
    font-size: 16.5px;
    font-weight: 400;
    line-height: 25px;
  }
  .specialties li { display: flex; align-items: center; gap: 12px; }
  .specialties li::before {
    content: "";
    width: 13px;
    height: 13px;
    border-radius: 50%;
    background: var(--teal);
    border: 2px solid var(--teal-light);
    flex: none;
  }
</style>
</head>
<body>

<section class="card card-front" aria-label="Business card front">
  <svg class="front-art" width="620" height="354" viewBox="0 0 620 354" aria-hidden="true">
    <rect x="478" y="34" width="112" height="104" fill="var(--teal)"/>
    <rect x="0" y="196" width="420" height="104" fill="var(--navy)"/>
    <circle cx="470" cy="138" r="112" fill="var(--white)"/>
    <circle cx="470" cy="138" r="96" fill="var(--teal-light)" stroke="var(--navy)" stroke-width="6"/>
  </svg>

  <div class="identity">
    <p class="identity-name">Dr. Rosalind Petrakis</p>
    <p class="identity-title">Licensed Psycholigist</p>
  </div>

  <ul class="contact-list">
    <li>
      <svg class="contact-icon" viewBox="0 0 16 16" aria-hidden="true"><path d="M3 1.5l3 3-1.6 2a9 9 0 0 0 5 5l2-1.6 3 3-2 2C6 14.5 1.5 10 1 3.5z" fill="var(--white)"/></svg>
      555.014.7788
    </li>
    <li>
      <svg class="contact-icon" viewBox="0 0 16 16" aria-hidden="true"><rect x="1" y="3" width="14" height="10" fill="none" stroke="var(--white)" stroke-width="1.6"/><path d="M1 3l7 6 7-6" fill="none" stroke="var(--white)" stroke-width="1.6"/></svg>
      ros@drrospetrakis.example
    </li>
    <li>
      <svg class="contact-icon" viewBox="0 0 16 16" aria-hidden="true"><circle cx="8" cy="8" r="6.5" fill="none" stroke="var(--white)" stroke-width="1.5"/><path d="M1.5 8h13M8 1.5c-3 3.5-3 9.5 0 13M8 1.5c3 3.5 3 9.5 0 13" fill="none" stroke="var(--white)" stroke-width="1.2"/></svg>
      drrospetrakis.example
    </li>
  </ul>

  <div class="logo-mark">Dr. Rosalind Petrakis</div>
</section>

<section class="card card-back" aria-label="Business card back">
  <div class="back-brand">
    <span class="back-brand-dot" aria-hidden="true"></span>
    <p class="back-brand-name">Dr. Rosalind<br>Petrakis</p>
  </div>

  <ul class="specialties">
    <li>Individual and Couples</li>
    <li>Relationships and Infidelity</li>
    <li>Sexual Health &amp; Aging</li>
    <li>Gender Identity &amp; Sexual Orientation</li>
    <li>Abuse and Trauma</li>
    <li>Sexual Compulsivity &amp; Addiction</li>
    <li>Sexual Dysfunction</li>
  </ul>
</section>

</body>
</html>
```